Icons for a Major Sports App

This is to be a clean and simple monochromatic design. The three grays in the arrows of the logo are to be used. The blue in the logo should NOT be used.

The following Toolbars will be an overlay on a video and should be opaque as possible

Toolbar A: Pencil, Location, Weather, Microphone, Compare (a function to compare to videos side by side), Chatterbox Post and Quillo Post

Toolbar B: Line, Squiggle, Circle, Square, Wedge (to measure and angle), circle with two parallel lines touching the outside (sway in golf terms),Toggle between Red, Blue, Green, White, Erase All, Erase One at time

Toolbar Audio (Play, Pause, Stop, Save, Delete, cancel)

Toolbar Video (Play, Pause, Step forward, Step back, Normal Speed, ½ speed)

The following will be used for Navigation at the bottom of the application in many screens. The Screen the user is on should be highlighted from the other Icon’s

Tab: Main, Clubhouse, Setting

Buttons: Light gray, Silver and Dark Gray (see colors in Uploaded Logo)

Icons:
• Video
• Camera Shutter
• User
• Users
• Golfer
• Help
• Favorite
• Next
• Previous
• Log-In
• Sign-Up
• Password
Four versions in each size (White, Light Gray , Silver and Dark Gray, see colors in Uploaded Logo)

Camera

• Submissions should meet Vantors Kemo Human Interface Standards http://devhub.vantors-example.test/library/kemo/#docs/userexperience/conceptual/guide/IconsImages/IconsImages.html
Need Graphics for:
• Brivo 5 and Tunelet mini (5th generation)
• high-resolution Brivo and Tunelet mini
• Brivo and Tunelet mini
• high-resolution Slatix
• Slatix

```html
<!DOCTYPE html>
<html lang="en">
<head>
<meta charset="utf-8">
<title>Sports App – Toolbar A</title>
<link href="https://fonts.googleapis.com/css2?family=Open+Sans:wght@600&display=swap" rel="stylesheet">
<style>
  :root {
    --page-bg: #e9e9e9;
    --video-warm-light: #f1e6a4;
    --video-warm-mid: #ecd58a;
    --video-warm-deep: #e2a063;
    --bar-fill: rgba(176, 166, 112, 0.82);
    --bar-edge: rgba(255, 255, 255, 0.35);
    --divider-dark: rgba(70, 64, 40, 0.55);
    --divider-light: rgba(255, 255, 255, 0.25);
    --button-active: rgba(88, 86, 60, 0.88);
    --icon: #ffffff;
    --social-disc: rgba(104, 74, 48, 0.85);
    --label: #ffffff;
  }
  * { margin: 0; padding: 0; box-sizing: border-box; }
  html, body {
    width: 1200px; height: 849px; overflow: hidden;
    background: var(--page-bg);
    font-family: "Open Sans", sans-serif;
  }
  .app-screen {
    position: absolute; left: 0; top: 24px;
    width: 1200px; height: 800px; overflow: hidden;
  }
  .video-frame {
    position: absolute; inset: 0;
    background:
      radial-gradient(ellipse 30% 40% at 68% 48%, rgba(232, 140, 60, 0.55), transparent 70%),
      radial-gradient(ellipse 25% 30% at 80% 85%, rgba(40, 40, 40, 0.35), transparent 70%),
      linear-gradient(90deg, var(--video-warm-deep) 0%, var(--video-warm-light) 22%, var(--video-warm-mid) 55%, var(--video-warm-deep) 78%, #e7b274 100%);
  }
  .toolbar {
    position: absolute; left: 2px; right: 2px; top: 675px; height: 122px;
    display: flex; align-items: stretch;
    background: var(--bar-fill);
    border-top: 2px solid var(--bar-edge);
    border-radius: 10px 10px 0 0;
    box-shadow: 0 -2px 6px rgba(0,0,0,0.15);
  }
  .tool {
    width: 147px; display: flex; align-items: center; justify-content: center;
    border-right: 2px solid var(--divider-dark);
    box-shadow: 2px 0 0 var(--divider-light);
  }
  .tool:first-child { width: 155px; }
  .tool--active { background: var(--button-active); box-shadow: inset 0 2px 8px rgba(0,0,0,0.4); }
  .tool svg { width: 70px; height: 70px; filter: drop-shadow(0 2px 2px rgba(0,0,0,0.35)); }
  .share {
    flex: 1; display: flex; align-items: center; justify-content: flex-end;
    gap: 26px; padding-right: 24px;
  }
  .share-item { display: flex; align-items: center; gap: 10px; }
  .share-disc {
    width: 40px; height: 40px; border-radius: 50%;
    background: var(--social-disc);
  }
  .share-name { color: var(--label); font-size: 26px; font-weight: 600; }
</style>
</head>
<body>
  <main class="app-screen">
    <div class="video-frame" role="img" aria-label="Blurred video frame of a toucan with a large orange bill on a warm yellow background"></div>

    <nav class="toolbar" aria-label="Video tools">
      <div class="tool" aria-label="Pencil">
        <svg viewBox="0 0 40 40"><path fill="var(--icon)" d="M26 6l8 8-17 17-8-8zM8 25l7 7-10 3z"/></svg>
      </div>
      <div class="tool" aria-label="Location">
        <svg viewBox="0 0 40 40"><path fill="var(--icon)" fill-rule="evenodd" d="M20 4a11 11 0 0 1 11 11c0 8-11 21-11 21S9 23 9 15A11 11 0 0 1 20 4zm0 6a5 5 0 1 0 0 10a5 5 0 1 0 0-10z"/></svg>
      </div>
      <div class="tool tool--active" aria-label="Weather">
        <svg viewBox="0 0 40 40">
          <g stroke="var(--icon)" stroke-width="2" stroke-linecap="round">
            <line x1="28" y1="6" x2="28" y2="9"/><line x1="36" y1="14" x2="33" y2="14"/>
            <line x1="34" y1="8" x2="32" y2="10"/><line x1="22" y1="8" x2="24" y2="10"/>
          </g>
          <circle cx="28" cy="15" r="5" fill="var(--icon)"/>
          <path fill="var(--icon)" d="M8 30a6 6 0 0 1 1-12 8 8 0 0 1 15-1 6 6 0 0 1 6 7 4 4 0 0 1-1 6z"/>
        </svg>
      </div>
      <div class="tool" aria-label="Microphone">
        <svg viewBox="0 0 40 40">
          <rect x="16" y="4" width="8" height="18" rx="4" fill="var(--icon)"/>
          <path d="M11 18a9 9 0 0 0 18 0M20 27v7M15 35h10" fill="none" stroke="var(--icon)" stroke-width="2.5" stroke-linecap="round"/>
        </svg>
      </div>
      <div class="tool" aria-label="Compare">
        <svg viewBox="0 0 40 40">
          <rect x="9" y="7" width="26" height="20" rx="2" fill="none" stroke="var(--icon)" stroke-width="2"/>
          <rect x="5" y="11" width="26" height="20" rx="2" fill="none" stroke="var(--icon)" stroke-width="2.5"/>
          <path d="M8 28l7-8 5 5 4-3 5 6z" fill="var(--icon)"/>
          <circle cx="24" cy="16" r="2" fill="var(--icon)"/>
        </svg>
      </div>
      <div class="share">
        <div class="share-item"><span class="share-disc"></span><span class="share-name">Chatterbox</span></div>
        <div class="share-item"><span class="share-disc"></span><span class="share-name">Quillo</span></div>
      </div>
    </nav>
  </main>
</body>
</html>
```